Business card design for global fintech startup

Veltrix is a modern payments platform for the global insurance industry, serving international health, life, and travel insurers, MGAs, brokers, and partners.

We need a professional, premium business card for use at insurance conferences and executive meetings. The goal is to create a card that feels trustworthy, modern, and high-quality, while still being distinctive and memorable in a stack of business cards.

Target audience:
Senior insurance executives (VP, C-suite).

Design goals:
Clear, professional, and credible
Modern but not trendy
Premium and well-structured
Easy to read and practical for networking

Brand direction:
Brand-first (company over individual)
Follow existing brand guidelines where possible
Clean layout, strong hierarchy, excellent readability

Must include:
Name
Title
Company name (Veltrix)
Logo
Email
Phone/Whatsapp
Website (www.withveltrix.example)
Tagline - Trust that moves money

Materials & finish:
Open to designer recommendations for premium look and feel.

Please avoid:
Flashy or trendy startup styles
Generic insurance icons or clichés
Cluttered layouts or hard-to-read text

Deliverables:
Front and back business card, print-ready files.

Target Market(s)

Global Insurance executives

Industry/Entity Type

Fintech, Insurtech, Insurance, Financial Services

Contact Information for Business Card

Name Title Company name (Veltrix) Logo Email Phone/Whatsapp Website (www.withveltrix.example) Tagline - Trust that moves money

Font styles to use
Other font styles liked:
• See brand guidelines

Requirements
Nice to have
• something that stands out/makes us more memorable while still remaining professional
Should not have
• Please avoid: Flashy or trendy startup styles Generic insurance icons or clichés Cluttered layouts or hard-to-read text

```html
<!DOCTYPE html>
<html lang="en">
<head>
<meta charset="UTF-8">
<title>Veltrix Business Card – Front and Back</title>
<link rel="stylesheet" href="https://fonts.googleapis.com/css2?family=Montserrat:wght@300;400;500;600&display=swap">
<style>
  :root {
    --ink: #231f20;
    --accent: #f58a34;
    --paper: #ffffff;
    --muted-on-ink: #bdb8b6;
    --card-edge: #c9c9c9;
    --canvas: #ffffff;
  }
  * { box-sizing: border-box; margin: 0; padding: 0; }
  html, body {
    width: 1200px;
    height: 1200px;
    overflow: hidden;
    background: var(--canvas);
    font-family: "Montserrat", Arial, sans-serif;
    color: var(--ink);
  }
  .sheet {
    position: relative;
    width: 1200px;
    height: 1200px;
  }
  .card {
    position: absolute;
    left: 300px;
    width: 600px;
    height: 384px;
  }
  .card--front {
    top: 180px;
    background: var(--paper);
    border: 1.5px solid var(--card-edge);
  }
  .card--back {
    top: 614px;
    background: var(--ink);
  }
  .wordmark {
    position: absolute;
    display: flex;
    align-items: center;
    gap: 14px;
    font-weight: 600;
    letter-spacing: 0.08em;
    line-height: 1;
  }
  .wordmark__dot {
    border-radius: 50%;
    background: var(--accent);
    flex: none;
  }
  .card--front .wordmark {
    left: 297px;
    top: 50px;
    font-size: 34px;
    color: var(--ink);
  }
  .card--front .wordmark__dot { width: 30px; height: 30px; }
  .card--back .wordmark {
    left: 0;
    right: 0;
    top: 160px;
    justify-content: center;
    font-size: 62px;
    color: var(--paper);
    gap: 22px;
  }
  .card--back .wordmark__dot { width: 56px; height: 56px; }
  .tagline {
    position: absolute;
    left: 0;
    right: 0;
    top: 300px;
    text-align: center;
    font-size: 14px;
    font-weight: 400;
    letter-spacing: 0.22em;
    text-transform: uppercase;
    color: var(--muted-on-ink);
  }

  .person {
    position: absolute;
    left: 59px;
    top: 185px;
  }
  .person__name {
    font-weight: 300;
    font-size: 24px;
    color: var(--accent);
    line-height: 1.2;
  }
  .person__title {
    margin-top: 6px;
    font-size: 14.5px;
    font-weight: 400;
    letter-spacing: 0.04em;
    text-transform: uppercase;
  }
  .contact {
    position: absolute;
    left: 297px;
    top: 190px;
    font-size: 15px;
    font-weight: 500;
    line-height: 26px;
  }
  .contact__group + .contact__group { margin-top: 32px; }
  .contact__web {
    color: var(--accent);
    font-weight: 400;
  }
</style>
</head>
<body>
  <main class="sheet">
    <section class="card card--front" aria-label="Business card front">
      <div class="wordmark">
        <span class="wordmark__dot"></span>
        <span class="wordmark__name">VELTRIX</span>
      </div>
      <div class="person">
        <p class="person__name">Full Name</p>
        <p class="person__title">Brand Director</p>
      </div>
      <div class="contact">
        <div class="contact__group">
          <p>full.name@withveltrix.example</p>
          <p>+1 123 456-7890</p>
        </div>
        <div class="contact__group">
          <p>123 Main Road, Suite 345</p>
          <p>East North, State 12345</p>
          <p class="contact__web">withveltrix.example</p>
        </div>
      </div>
    </section>

    <section class="card card--back" aria-label="Business card back">
      <div class="wordmark">
        <span class="wordmark__dot"></span>
        <span class="wordmark__name">VELTRIX</span>
      </div>
      <p class="tagline">Trust that moves money</p>
    </section>
  </main>
</body>
</html>
```